Fun modern label needed for olive oil bottle

I need a label for a boutique handmade olive oil line. It needs to be fun and reflect the smallness of the operation and from rural Australia

The name of the line comes from the fact that I live in rural Australia and the black tar road ends 5 km from my home. The road turns to dusty slippery gravel in summer and wet and slippery gravel mud in winter.
Those of us who live out here say that the best people live WATTLE CREEK HOLLOW.

There are no restrictions on colours but it MUST be fun with clear strong lines.

The label is rectangular with the short sides top and bottom. I shall measure the bottles later today and update the brief for you

Below is an example of the bottles used and there will be 3 different sizes
Updates

I have added a couple of photos to show Australian labels and what is need on them sorry to have left out this crucial information

Industry/Entity Type

Boutique

Requirements
Must have
• Wattle Creek Hollow as name
Some sort of logo

```html
<!DOCTYPE html>
<html lang="en">
<head>
<meta charset="utf-8">
<title>Wattle Creek Hollow – Extra Virgin Olive Oil Labels</title>
<link rel="stylesheet" href="https://fonts.googleapis.com/css2?family=Jura:wght@400;600&family=Open+Sans:wght@400;600&display=swap">
<style>
  :root {
    --page-bg: #eef0ea;
    --label-white: #ffffff;
    --label-silver: #d9dcdc;
    --glass-olive: #8c8139;
    --glass-olive-mid: #7a7030;
    --glass-olive-dark: #5c5522;
    --leaf-green: #5fc21a;
    --leaf-green-light: #b6f06a;
    --brand-green: #3f8f1c;
    --band-green: #66d61a;
    --band-green-light: #b8ef7a;
    --ink: #1c1c1a;
    --ink-on-glass: #12110a;
  }
  * { box-sizing: border-box; margin: 0; padding: 0; }
  html, body {
    width: 1176px;
    height: 1200px;
    overflow: hidden;
    background: var(--page-bg);
  }
  .canvas {
    position: relative;
    width: 1176px;
    height: 1200px;
  }
  .label {
    position: absolute;
    top: 42px;
    width: 340px;
    height: 1115px;
    border-radius: 30px;
    overflow: hidden;
  }
  .label--white {
    left: 200px;
    background: linear-gradient(to bottom, var(--label-silver) 0%, var(--label-white) 45%, var(--label-white) 100%);
  }
  .label--clear {
    left: 636px;
    background: linear-gradient(to right, var(--glass-olive-dark) 0%, var(--glass-olive-mid) 12%, var(--glass-olive) 30%, var(--glass-olive) 75%, var(--glass-olive-mid) 90%, var(--glass-olive-dark) 100%);
  }
  .brand {
    position: absolute;
    top: 34px;
    left: 26px;
    display: flex;
    align-items: center;
    gap: 16px;
  }
  .brand__dot {
    width: 110px;
    height: 110px;
    border-radius: 50%;
    background: var(--brand-green);
    flex: none;
  }
  .brand__name {
    font-family: "Jura", sans-serif;
    font-weight: 600;
    font-size: 24px;
    line-height: 1.15;
    letter-spacing: 1px;
    color: var(--brand-green);
  }
  .label--clear .brand__name { color: var(--leaf-green-light); }
  .olive-sprig {
    position: absolute;
    top: 190px;
    left: 50px;
    width: 260px;
    height: 320px;
  }
  .product {
    position: absolute;
    top: 560px;
    left: 0;
    width: 100%;
    text-align: center;
    color: var(--ink);
  }
  .label--clear .product { color: var(--ink-on-glass); }
  .product__grade {
    font-family: "Open Sans", sans-serif;
    font-size: 27px;
  }
  .product__name {
    font-family: "Jura", sans-serif;
    font-weight: 400;
    font-size: 62px;
    line-height: 1.1;
    letter-spacing: 1px;
  }
  .product__origin {
    margin-top: 10px;
    font-family: "Open Sans", sans-serif;
    font-weight: 600;
    font-size: 16px;
  }
  .label__band {
    position: absolute;
    left: 0;
    bottom: 0;
    width: 100%;
    height: 190px;
    background: linear-gradient(to bottom, var(--band-green-light) 0%, var(--band-green) 12%, var(--band-green) 100%);
  }
  .label--clear .label__band { background: var(--band-green); }
</style>
</head>
<body>
<main class="canvas">
  <section class="label label--white">
    <div class="brand">
      <span class="brand__dot"></span>
      <span class="brand__name">WATTLE<br>CREEK<br>HOLLOW</span>
    </div>
    <svg class="olive-sprig" viewBox="0 0 260 320" role="img" aria-label="Illustration of an olive sprig with two green leaves and two black olives">
      <defs>
        <linearGradient id="sprigWhite" x1="0" y1="0" x2="0" y2="1">
          <stop offset="0" stop-color="#8fdc40"/>
          <stop offset="1" stop-color="#4fb514"/>
        </linearGradient>
      </defs>
      <rect x="0" y="0" width="260" height="320" rx="40" fill="url(#sprigWhite)"/>
    </svg>
    <div class="product">
      <p class="product__grade">Extra Virgin</p>
      <h1 class="product__name">OLIVE OIL</h1>
      <p class="product__origin">Made in Australia</p>
    </div>
    <div class="label__band"></div>
  </section>

  <section class="label label--clear">
    <div class="brand">
      <span class="brand__dot"></span>
      <span class="brand__name">WATTLE<br>CREEK<br>HOLLOW</span>
    </div>
    <svg class="olive-sprig" viewBox="0 0 260 320" role="img" aria-label="Illustration of an olive sprig with two green leaves and two black olives">
      <defs>
        <linearGradient id="sprigClear" x1="0" y1="0" x2="0" y2="1">
          <stop offset="0" stop-color="#8fdc40"/>
          <stop offset="1" stop-color="#4fb514"/>
        </linearGradient>
      </defs>
      <rect x="0" y="0" width="260" height="320" rx="40" fill="url(#sprigClear)"/>
    </svg>
    <div class="product">
      <p class="product__grade">Extra Virgin</p>
      <h2 class="product__name">OLIVE OIL</h2>
      <p class="product__origin">Made in Australia</p>
    </div>
    <div class="label__band"></div>
  </section>
</main>
</body>
</html>
```